Retail Product - 50ct Disinfectant Wipes

We are making a 50 count disinfectant wipe. We want to have our "Tarnvale Goods" logo (attached the project files) on it, the
number of wipes "50 Count". It needs to fit inside the attached die-line (which shows the actual dimensions
of the product and is attached in the project files) and should revolve around the cut-out in the center that the wipes are taken from.

The product name is "Disinfectant Wipes".

We are very open with color scheme, artistic style, etc. but it needs to only use things created by you, the artist,
or something in the public domain.

Please leave a place-holder for a UPC-A barcode.

```html
<!DOCTYPE html>
<html lang="en">
<head>
<meta charset="utf-8">
<title>Tarnvale Goods Disinfecting Wipes – Front Panel</title>
<link href="https://fonts.googleapis.com/css2?family=Montserrat:wght@300;400;700;800&display=swap" rel="stylesheet">
<style>
  :root {
    --stage: #333333;
    --white: #ffffff;
    --ink: #111111;
    --sun-light: #fff6b8;
    --sun: #ffe13a;
    --sun-deep: #ffc400;
    --window: #6e819b;
    --badge: #2fb3e6;
    --rule: #9a9a9a;
  }
  html, body {
    margin: 0;
    padding: 0;
    width: 1200px;
    height: 727px;
    overflow: hidden;
    background: var(--stage);
    font-family: "Montserrat", sans-serif;
  }
  .front-panel {
    position: absolute;
    left: 30px;
    top: 107px;
    width: 1140px;
    height: 513px;
    overflow: hidden;
    background: linear-gradient(110deg, var(--sun-light) 30%, var(--sun) 70%, var(--sun-deep) 100%);
  }
  .panel-art {
    position: absolute;
    inset: 0;
  }
  .brand-name {
    position: absolute;
    left: 40px;
    top: 224px;
    width: 250px;
    display: flex;
    align-items: center;
    gap: 12px;
    color: var(--ink);
    font-weight: 800;
    font-size: 30px;
    line-height: 1.05;
    letter-spacing: 1px;
    text-transform: uppercase;
  }
  .brand-dot {
    flex: none;
    width: 22px;
    height: 22px;
    border-radius: 50%;
    background: var(--badge);
  }
  .barcode-placeholder {
    position: absolute;
    left: 40px;
    top: 30px;
    width: 110px;
    height: 56px;
    background: var(--white);
    border: 1px solid var(--rule);
    box-sizing: border-box;
  }
  .product-title {
    margin: 0;
    color: var(--ink);
    line-height: 1;
  }
  .title-main {
    position: absolute;
    left: 622px;
    top: 44px;
    font-weight: 800;
    font-size: 50px;
    letter-spacing: 1px;
    white-space: nowrap;
  }
  .title-sub {
    position: absolute;
    left: 834px;
    top: 84px;
    font-weight: 300;
    font-size: 76px;
    letter-spacing: 2px;
    white-space: nowrap;
  }
  .surface-note {
    position: absolute;
    right: 28px;
    top: 334px;
    margin: 0;
    text-align: right;
    font-weight: 400;
    font-size: 19px;
    line-height: 25px;
    color: var(--ink);
    text-transform: uppercase;
  }
  .count-badge {
    position: absolute;
    left: 959px;
    top: 451px;
    width: 168px;
    height: 38px;
    background: var(--badge);
    clip-path: polygon(12px 0, 100% 0, 100% 100%, 12px 100%, 0 50%);
    color: var(--white);
    font-weight: 700;
    font-size: 27px;
    line-height: 38px;
    text-align: right;
    padding-right: 16px;
    box-sizing: border-box;
  }
</style>
</head>
<body>
  <main class="front-panel">
    <svg class="panel-art" viewBox="0 0 1140 513" width="1140" height="513">
      <defs>
        <radialGradient id="glow" cx="0.55" cy="0.75" r="0.5">
          <stop offset="0" stop-color="#ffffff" stop-opacity="0.8"/>
          <stop offset="1" stop-color="#ffffff" stop-opacity="0"/>
        </radialGradient>
        <linearGradient id="whiteSweep" x1="0" y1="0" x2="1" y2="0.3">
          <stop offset="0.4" stop-color="#ffffff"/>
          <stop offset="1" stop-color="#e6e6e6"/>
        </linearGradient>
      </defs>
      <rect class="soft-glow" x="0" y="0" width="1140" height="513" fill="url(#glow)"/>
      <path class="white-sweep" d="M0 0 H792 Q840 60 770 130 L420 300 Q200 380 103 513 H0 Z" fill="url(#whiteSweep)"/>
      <path class="dispenser-window" fill="#6e819b" stroke="#ffffff" stroke-width="2"
        d="M420 130 H792 Q818 130 818 156 V357 Q818 383 792 383 H420 Q400 383 388 365 L368 330 Q358 316 342 313 Q310 300 310 257 Q310 214 342 201 Q358 198 368 184 L388 148 Q400 130 420 130 Z"/>
    </svg>

    <div class="barcode-placeholder" role="img" aria-label="UPC-A barcode placeholder"></div>

    <div class="brand-name"><span class="brand-dot"></span><span>Tarnvale<br>Goods</span></div>

    <h1 class="product-title">
      <span class="title-main">DISINFECTING</span>
      <span class="title-sub">WIPES</span>
    </h1>

    <p class="surface-note">Safe on finished wood,<br>sealed granite and<br>stainless steel</p>

    <div class="count-badge">50 Count</div>
  </main>
</body>
</html>
```